Modern Website Design for PollMeridian – CX & Loyalty SaaS Platform

We need a modern, professional, and responsive website design for our B2B SaaS platform, PollMeridian. We help companies collect real-time customer feedback, analyze insights, and improve loyalty — combining a powerful CX platform with expert consulting services. The website should clearly communicate who we are and what we offer within the first impression. It should balance data-driven visuals such as dashboards, analytics, and charts with a human, approachable feel. The design must include at least six key pages: Homepage, Product/Services, About, Blog/Resources, Contact/Demo, and Pricing. It should be conversion-focused with clear calls-to-action that encourage visitors to request a demo or contact us. The site must be fully responsive across desktop, tablet, and mobile. It should support multiple languages, starting with English and Danish. Most importantly, the delivery must be a final WordPress website, ready to go live, not just design files.

Target Market(s)

Our target market is medium-to-large B2B organizations. The primary audience includes CX leaders, executives, and managers in customer success and service who want to measure loyalty, understand customer insights, and improve retention.

Industry/Entity Type

Technology / SaaS / Customer Experience

Coding

Coded - Design and coding required

Number of Pages Required

5+ page

Font styles to use
Sans Serif

Requirements
Must have
• The project must deliver a final WordPress website that is fully responsive across all devices. The design should be clean, modern, and SaaS-inspired, with clear calls-to-action on every page. It must also support English and Danish, with a visible language toggle. The site should include visuals of dashboards and analytics that reflect data-driven insights. It must feature sections for case studies or testimonials to build trust. The copywriting should be SEO-friendly, and the design should include smooth animations or hover effects that add polish without making the website feel heavy.
Should not have
• Cluttered layouts, or generic stock photos such as handshakes

```html
<!DOCTYPE html>
<html lang="en">
<head>
<meta charset="utf-8">
<title>PollMeridian – CX &amp; Loyalty Platform</title>
<link href="https://fonts.googleapis.com/css2?family=Inter:wght@400;500;600;700;800&display=swap" rel="stylesheet">
<style>
:root{
  --blue:#2b7de3;
  --blue-dark:#1a5fc4;
  --navy:#0f1b3d;
  --text:#1c2440;
  --muted:#5a6480;
  --band:#dcebfb;
  --hero:#e6f0fc;
  --footer:#0f2249;
  --white:#ffffff;
  --gold:#f5c518;
  --line:#dde5f2;
}
*{box-sizing:border-box;margin:0;padding:0}
html,body{width:1200px;height:4577px;overflow:hidden}
body{font-family:"Inter",sans-serif;color:var(--text);background:var(--white);position:relative}
.abs{position:absolute}
.btn{position:absolute;display:flex;align-items:center;justify-content:center;font-size:12px;font-weight:500;text-transform:uppercase;border-radius:6px;height:48px;letter-spacing:.2px}
.btn-primary{background:var(--blue);color:var(--white)}
.btn-outline{border:1.5px solid var(--navy);color:var(--navy);background:var(--white)}
.brand{display:flex;align-items:center;gap:10px;font-size:24px;font-weight:600;color:var(--blue);letter-spacing:1px}
.brand-dot{width:34px;height:34px;border-radius:50%;background:var(--blue)}
h2.section-title{position:absolute;left:0;width:1200px;text-align:center;font-size:40px;font-weight:500;color:var(--navy);line-height:1.18}
.section-sub{position:absolute;left:0;width:1200px;text-align:center;font-size:13px;color:var(--muted);line-height:1.7}

/* hero */
.hero{position:absolute;top:0;left:0;width:1200px;height:580px;background:linear-gradient(180deg,var(--hero) 0%,#f4f8fe 70%,#fff 100%)}
.nav{position:absolute;top:18px;left:140px;width:1060px;height:46px;display:flex;align-items:center}
.nav-links{position:absolute;left:296px;display:flex;gap:20px;font-size:13px;font-weight:500;color:var(--navy)}
.nav-demo{position:absolute;left:622px;top:2px;width:150px;height:42px;border-radius:6px;background:var(--blue);color:#fff;font-size:13px;display:flex;align-items:center;justify-content:center}
.nav-login{position:absolute;left:783px;top:2px;width:78px;height:42px;border:1.5px solid var(--navy);border-radius:6px;font-size:13px;display:flex;align-items:center;justify-content:center}
.nav-lang{position:absolute;left:870px;font-size:12px;color:var(--navy)}
.nav-lang span{color:#8a93aa}
.hero h1{position:absolute;left:140px;top:124px;font-size:48px;line-height:48px;font-weight:500;color:var(--navy);letter-spacing:-.5px}
.hero h1 b{font-weight:800}
.hero p{position:absolute;left:140px;top:282px;width:460px;font-size:17px;line-height:24px;color:#2a3352}

.dash{position:absolute;left:667px;top:115px;width:560px;height:370px;background:#eef4fc;border-radius:12px;box-shadow:0 10px 40px rgba(30,80,160,.15)}
.dash-inner{position:absolute;left:16px;top:42px;width:540px;height:322px;background:#fff;border-radius:8px}
.dash-side{position:absolute;left:8px;top:8px;width:120px;height:306px;font-size:8px;color:#3b4566}
.dash-side .menu{position:absolute;left:12px;top:48px;width:94px;height:140px;background:var(--blue);border-radius:8px}
.card-s{position:absolute;background:#fff;border-radius:8px;border:1px solid var(--line)}

/* features */
.fcard{position:absolute;width:288px;height:196px;background:#fff;border-radius:10px;box-shadow:0 6px 24px rgba(40,80,150,.12);text-align:center}
.fcard h3{margin-top:68px;font-size:17px;font-weight:600;color:var(--navy)}
.fcard p{margin:12px 18px 0;font-size:12.5px;line-height:23px;color:#333b55}
.ficon{position:absolute;left:100px;top:-48px;width:88px;height:88px;border-radius:50%;background:linear-gradient(160deg,#3d8ff0,#1a5fc4);border:5px solid #fff;box-shadow:0 6px 16px rgba(30,90,190,.3);display:flex;align-items:center;justify-content:center}

/* about */
.about{position:absolute;top:1511px;left:0;width:1200px;height:566px;background:var(--band)}
.about h2{position:absolute;left:661px;top:105px;font-size:42px;font-weight:500;color:var(--navy)}
.about p{position:absolute;left:662px;width:400px;font-size:12.5px;line-height:21px;color:#3c4562}

/* why */
.why-item{position:absolute;font-size:17px;font-weight:500;color:var(--navy);line-height:22px}
.why-icon{position:absolute;width:62px;height:62px;border-radius:12px;background:#fff;box-shadow:0 6px 18px rgba(40,80,150,.14);display:flex;align-items:center;justify-content:center}

/* testimonials */
.clients{position:absolute;top:2688px;left:0;width:1200px;height:642px;background:var(--band);overflow:hidden}
.tcard{position:absolute;top:196px;width:444px;height:288px;background:#fff;border-radius:22px;text-align:center;box-shadow:0 4px 20px rgba(40,80,150,.08)}
.tcard .quote{margin-top:34px;font-size:58px;line-height:40px;color:var(--blue);font-weight:800;height:36px}
.tcard .stars{margin-top:12px;color:var(--gold);font-size:15px;letter-spacing:3px}
.tcard p{margin:12px 30px 0;font-size:13.5px;line-height:25.5px;color:#2b3350}
.tcard .name{margin-top:14px;font-size:14px;font-weight:600;color:var(--navy)}

/* trusted */
.logo-box{position:absolute;top:3515px;width:134px;height:86px;background:#fff;border-radius:8px;box-shadow:0 4px 14px rgba(40,80,150,.14);display:flex;align-items:center;justify-content:center;gap:7px;font-size:15px;font-weight:600;color:var(--navy)}
.logo-box i{width:14px;height:14px;border-radius:50%;background:var(--blue);display:block}

/* cta */
.cta{position:absolute;left:140px;top:3743px;width:920px;height:382px;border-radius:28px;background:radial-gradient(ellipse at 80% 90%,#2f8ff0 0%,transparent 55%),linear-gradient(120deg,#0d2c78 0%,#1748a8 50%,#1f6fd6 100%);text-align:center;color:#fff}
.cta h2{position:absolute;top:82px;width:100%;font-size:40px;line-height:48px;font-weight:400}
.cta h2 b{font-weight:700}
.cta p{position:absolute;top:188px;left:180px;width:560px;font-size:13px;line-height:22px;color:#e4ecff}

/* footer */
.footer{position:absolute;top:4205px;left:0;width:1200px;height:372px;background:var(--footer);color:#fff}
.footer h4{position:absolute;top:68px;font-size:17px;font-weight:500}
.footer ul{position:absolute;top:110px;list-style:none;font-size:13px;line-height:27px;color:#dfe6f5}
.fcontact{position:absolute;left:684px;font-size:13px;line-height:20px;color:#dfe6f5}
.social{position:absolute;left:956px;display:flex;align-items:center;gap:10px;font-size:13px;color:#dfe6f5}
.social i{width:28px;height:28px;border-radius:50%;border:1.5px solid #dfe6f5;display:block}
</style>
</head>
<body>

<!-- HERO -->
<section class="hero">
  <nav class="nav">
    <div class="brand"><span class="brand-dot"></span>Lumora CX</div>
    <div class="nav-links"><span>Product</span><span>About</span><span>Resources</span><span>Pricing</span><span>Contact</span></div>
    <div class="nav-demo">Request A Demo</div>
    <div class="nav-login">Login</div>
    <div class="nav-lang">EN | <span>DA</span></div>
  </nav>
  <h1>Transform Customer<br>Feedback Into<br><b>Actionable Insights</b></h1>
  <p>Real-time feedback collection, expert insights, and leadership-ready reporting. Unlike software-only tools, we combine powerful CX technology with dedicated consulting services.</p>
  <div class="btn btn-primary" style="left:140px;top:400px;width:150px">Request A Demo</div>
  <div class="btn btn-outline" style="left:303px;top:400px;width:122px">Learn More</div>

  <div class="dash" aria-label="Dashboard preview">
    <div class="abs" style="left:26px;top:10px;font-size:10px;color:var(--blue);font-weight:600">● Lumora CX</div>
    <div class="abs" style="left:266px;top:10px;width:226px;height:22px;background:#fff;border-radius:5px;font-size:8px;padding:6px 8px;color:#555">Search here</div>
    <div class="dash-inner">
      <div class="dash-side">
        <div style="position:absolute;left:10px;top:6px;color:var(--blue);font-weight:600">● Lumora CX</div>
        <div style="position:absolute;left:10px;top:30px;color:#999">MENU</div>
        <div class="menu">
          <div style="margin:6px;background:#fff;border-radius:4px;height:16px;font-size:7px;padding:4px 10px;color:var(--blue)">Profile</div>
          <div style="color:#fff;font-size:7px;line-height:20px;padding-left:20px">Payroll<br>Attendance<br>Performance<br>Time-off</div>
        </div>
        <div style="position:absolute;left:14px;top:200px;line-height:21px">Projects<br>Teams<br>Schedule<br>Analytics</div>
      </div>
      <div class="abs" style="left:142px;top:34px;font-size:7px;color:#888">Good Morning</div>
      <div class="abs" style="left:142px;top:44px;font-size:10px;font-weight:600;color:var(--navy)">Nordvik Labs</div>
      <div class="card-s" style="left:140px;top:80px;width:290px;height:180px">
        <div class="abs" style="left:12px;top:12px;font-size:10px;font-weight:500">Attendance rate</div>
        <div class="abs" style="left:12px;top:26px;font-size:6px;color:#999">Total attendance of staff this month</div>
        <div class="abs" style="left:12px;top:70px;font-size:15px;font-weight:700">8.35%</div>
        <div class="abs" style="left:12px;top:140px;font-size:7px;line-height:15px"><span style="color:var(--blue)">●</span> On-time<br><span style="color:var(--gold)">●</span> Late<br><span style="color:#ccc">●</span> Absent</div>
        <svg class="abs" style="left:130px;top:60px" width="150" height="110" viewBox="0 0 150 110">
          <g fill="#2b7de3">
            <rect x="0" y="50" width="10" height="50" rx="5"/><rect x="14" y="40" width="10" height="60" rx="5"/><rect x="28" y="60" width="10" height="40" rx="5"/><rect x="42" y="30" width="10" height="70" rx="5"/><rect x="56" y="55" width="10" height="45" rx="5"/><rect x="70" y="20" width="10" height="80" rx="5"/><rect x="84" y="45" width="10" height="55" rx="5"/><rect x="98" y="35" width="10" height="65" rx="5"/><rect x="112" y="50" width="10" height="50" rx="5"/><rect x="126" y="60" width="10" height="40" rx="5"/>
          </g>
          <g fill="#c7e23a"><circle cx="5" cy="42" r="4"/><circle cx="47" cy="22" r="4"/><circle cx="75" cy="12" r="4"/><circle cx="103" cy="27" r="4"/></g>
        </svg>
      </div>
      <div class="card-s" style="left:140px;top:268px;width:290px;height:50px"><div style="margin:12px;font-size:10px">Recent payroll</div></div>
      <div class="card-s" style="left:440px;top:80px;width:100px;height:238px">
        <div style="margin:8px;font-size:10px">Schedule</div>
        <div class="abs" style="left:10px;top:110px;width:22px;height:110px;border-radius:11px;background:var(--blue)"></div>
      </div>
    </div>
  </div>
</section>

<!-- FEATURES -->
<section>
  <h2 class="section-title" style="top:634px">Powerful Features for<br>CX Excellence</h2>
  <p class="section-sub" style="top:738px">Our comprehensive platform provides everything you need to measure,<br>understand, and improve customer experience</p>

  <div class="fcard" style="left:142px;top:862px"><div class="ficon"><svg width="40" height="40" viewBox="0 0 40 40" fill="#fff"><rect x="4" y="24" width="6" height="12"/><rect x="13" y="18" width="6" height="18"/><rect x="22" y="12" width="6" height="24"/><path d="M4 16 L16 8 L24 12 L36 4" stroke="#fff" stroke-width="2.5" fill="none"/></svg></div><h3>Real-Time Analytics</h3><p>Access Instant Insights With Our Live Dashboards And Customizable Reports That Track Key CX Metrics.</p></div>
  <div class="fcard" style="left:456px;top:862px"><div class="ficon"><svg width="40" height="40" viewBox="0 0 40 40" fill="none" stroke="#fff" stroke-width="2.5"><circle cx="20" cy="20" r="14"/><circle cx="20" cy="20" r="6"/><circle cx="20" cy="6" r="3" fill="#fff"/><circle cx="34" cy="20" r="3" fill="#fff"/><circle cx="6" cy="20" r="3" fill="#fff"/></svg></div><h3>Multi-Channel Feedback</h3><p>Collect Feedback Across Email, In-App, SMS, And More With Seamless Integration Options.</p></div>
  <div class="fcard" style="left:770px;top:862px"><div class="ficon"><svg width="40" height="40" viewBox="0 0 40 40" fill="#fff" stroke="#fff" stroke-width="2"><circle cx="10" cy="20" r="5"/><circle cx="30" cy="8" r="3"/><circle cx="32" cy="20" r="3"/><circle cx="30" cy="32" r="3"/><path d="M15 20 H29 M14 17 L27 9 M14 23 L27 31" fill="none"/></svg></div><h3>AI-Powered Insights</h3><p>Our Advanced AI Analyzes Open-Ended Responses To Uncover Trends And Sentiment Drivers.</p></div>

  <div class="fcard" style="left:142px;top:1134px"><div class="ficon"><svg width="40" height="40" viewBox="0 0 40 40" fill="none" stroke="#fff" stroke-width="2.5"><rect x="4" y="6" width="32" height="22" rx="2"/><path d="M14 36 H26 M20 28 V36"/><path d="M10 22 V16 M16 22 V12 M22 22 V14 M28 22 V10"/></svg></div><h3>Role-Based Dashboards</h3><p>Custom Views For Executives, Managers, And Frontline Staff With Relevant KPIs And Alerts.</p></div>
  <div class="fcard" style="left:456px;top:1134px"><div class="ficon"><svg width="40" height="40" viewBox="0 0 40 40" fill="none" stroke="#fff" stroke-width="3"><path d="M12 6 V34 M20 10 V30 M28 6 L34 20 L28 34"/></svg></div><h3>Loyalty Measurement</h3><p>Track NPS, CSAT, CES And Other Loyalty Metrics With Industry Benchmarking.</p></div>
  <div class="fcard" style="left:770px;top:1134px"><div class="ficon"><svg width="40" height="40" viewBox="0 0 40 40" fill="#fff"><circle cx="13" cy="14" r="5"/><path d="M4 32 Q13 20 22 32Z"/><rect x="22" y="6" width="14" height="10" rx="2"/><rect x="20" y="26" width="16" height="8"/></svg></div><h3>Expert Consultation</h3><p>Our CX Specialists Help You Interpret Data And Develop Effective Improvement Strategies.</p></div>

  <div class="btn btn-primary" style="left:458px;top:1374px;width:150px">Request A Demo</div>
  <div class="btn btn-outline" style="left:621px;top:1374px;width:122px">Learn More</div>
</section>

<!-- ABOUT -->
<section class="about">
  <div class="abs" role="img" aria-label="Photo of three colleagues reviewing customer data on a tablet" style="left:140px;top:80px;width:284px;height:400px;border-radius:6px;background:linear-gradient(150deg,#c9d6e4 0%,#8fa6bf 45%,#6d5f56 100%)"></div>
  <div class="abs" style="left:443px;top:82px;width:154px;height:167px;background:var(--blue);border-radius:6px;color:#fff;text-align:center">
    <svg style="margin-top:24px" width="58" height="38" viewBox="0 0 58 38" fill="none" stroke="#fff" stroke-width="3"><path d="M4 14 L16 4 L28 12 L40 4 L54 14 L40 30 L28 22 L16 30Z"/></svg>
    <div style="font-size:38px;font-weight:700;line-height:44px">15+</div>
    <div style="font-size:11px;margin-top:4px">YEAR OF EXPERIENCE</div>
  </div>
  <div class="abs" role="img" aria-label="Illustration of cloud data on a circuit board" style="left:364px;top:260px;width:234px;height:170px;border-radius:6px;border:4px solid #fff;background:radial-gradient(circle at 55% 45%,#7fd6ff 0%,#1d74b8 35%,#0c2f5a 80%)"></div>
  <h2>About Lumora-CX</h2>
  <p style="top:162px">Our mission is to empower businesses with the tools and expertise to build lasting customer relationships. Founded by CX innovators, we combine cutting-edge technology with human insights to drive measurable results.</p>
  <p style="top:250px">With over a decade of experience helping businesses transform their operations, we understand that every organization has unique challenges and goals. Our team of experts works closely with you to deliver solutions that not only meet your current needs but scale with your future growth.</p>
  <div class="btn btn-primary" style="left:662px;top:379px;width:152px">Request A Demo</div>
  <div class="btn btn-outline" style="left:826px;top:379px;width:122px">Learn More</div>
</section>

<!-- WHY -->
<section>
  <h2 class="section-title" style="top:2152px">Why Choose Lumora-CX?</h2>
  <p class="section-sub" style="top:2212px">Discover the features that make our solution the right choice for businesses<br>looking to optimize their workflow and boost productivity.</p>
  <svg class="abs" style="left:0;top:2250px" width="1200" height="320" viewBox="0 0 1200 320" fill="none">
    <circle cx="597" cy="162" r="170" fill="#f3f7fd"/>
    <circle cx="597" cy="162" r="110" fill="#e9f1fc"/>
    <path d="M413 73 H445 V130 H530 M413 233 H445 V180 H530 M780 73 H752 V130 H664 M780 233 H752 V180 H664" stroke="#c7d3e6" stroke-width="1.5"/>
    <g fill="var(--blue)"><circle cx="413" cy="73" r="4"/><circle cx="413" cy="233" r="4"/><circle cx="780" cy="73" r="4"/><circle cx="780" cy="233" r="4"/></g>
    <circle cx="597" cy="162" r="62" fill="#fff" style="filter:drop-shadow(0 6px 14px rgba(40,80,150,.18))"/>
    <circle cx="597" cy="162" r="20" fill="var(--blue)"/>
  </svg>
  <div class="why-item" style="left:140px;top:2306px;width:190px;text-align:right">The Power Of Software<br>+ Expert Guidance</div>
  <div class="why-icon" style="left:348px;top:2292px"><svg width="34" height="34" viewBox="0 0 34 34" fill="none" stroke="var(--blue)" stroke-width="2.5"><circle cx="17" cy="15" r="6"/><path d="M17 3 V7 M17 23 V27 M5 15 H9 M25 15 H29"/><path d="M4 31 H30"/></svg></div>
  <div class="why-item" style="left:140px;top:2469px;width:190px;text-align:right">Move From Insight To<br>Action, Faster</div>
  <div class="why-icon" style="left:348px;top:2454px"><svg width="34" height="34" viewBox="0 0 34 34" fill="none" stroke="var(--blue)" stroke-width="2.5"><circle cx="17" cy="17" r="13"/><circle cx="17" cy="17" r="5"/><path d="M17 4 V10 M17 24 V30"/></svg></div>
  <div class="why-icon" style="left:784px;top:2290px"><svg width="34" height="34" viewBox="0 0 34 34" fill="none" stroke="var(--blue)" stroke-width="2.5"><circle cx="17" cy="17" r="13"/><path d="M8 18 L14 12 L20 16 L26 12"/></svg></div>
  <div class="why-item" style="left:856px;top:2302px;width:220px">Strengthen Relationships<br>At Every Touchpoint</div>
  <div class="why-icon" style="left:784px;top:2458px"><svg width="34" height="34" viewBox="0 0 34 34" fill="none" stroke="var(--blue)" stroke-width="2.5"><circle cx="15" cy="21" r="9"/><path d="M15 16 V26 M22 6 L30 4 L28 12"/></svg></div>
  <div class="why-item" style="left:868px;top:2472px;width:200px">Protect Revenue And<br>Reduce Customer<br>Churn</div>
  <div class="btn btn-primary" style="left:458px;top:2557px;width:150px">Request A Demo</div>
  <div class="btn btn-outline" style="left:621px;top:2557px;width:122px">Learn More</div>
</section>

<!-- TESTIMONIALS -->
<section class="clients">
  <h2 class="section-title" style="top:76px">What Our Clients Say</h2>
  <p class="section-sub" style="top:138px">Hear from businesses that have transformed their customer experience with PollMeridian.</p>
  <div class="tcard" style="left:-332px"><div class="quote">“</div><div class="stars">★★★★★</div><p>Lorem Ipsum Is Simply Dummy Text Of The Printing And Typesetting Industry. Lorem Ipsum Has Been The Industry's Standard Dummy Text Ever Since The 1500s, When An Unknown Printer Took A Galley Of Type And Scrambled It To Make A Type Specimen Book. It Has Five Centuries...</p></div>
  <div class="tcard" style="left:140px"><div class="quote">“</div><div class="stars">★★★★★</div><p>Lorem Ipsum Is Simply Dummy Text Of The Printing And Typesetting Industry. Lorem Ipsum Has Been The Industry's Standard Dummy Text Ever Since The 1500s, When An Unknown Printer Took A Galley Of Type And Scrambled It To Make A Type Specimen Book. It Has Five Centuries...</p><div class="name">Clara Jensen</div></div>
  <div class="tcard" style="left:612px"><div class="quote">“</div><div class="stars">★★★★★</div><p>Lorem Ipsum Is Simply Dummy Text Of The Printing And Typesetting Industry. Lorem Ipsum Has Been The Industry's Standard Dummy Text Ever Since The 1500s, When An Unknown Printer Took A Galley Of Type And Scrambled It To Make A Type Specimen Book. It Has Five Centuries...</p><div class="name">Mikkel Hansen</div></div>
  <div class="tcard" style="left:1088px"><div class="quote">“</div><div class="stars">★★★★★</div><p>Lorem Ipsum Is Simply Dummy Text Of The Printing And Typesetting Industry. Lorem Ipsum Has Been The Industry's Standard Dummy Text Ever Since The 1500s, When An Unknown Printer Took A Galley Of Type And Scrambled It To Make A Type Specimen Book.</p></div>
  <svg class="abs" style="left:554px;top:515px" width="92" height="42" viewBox="0 0 92 42"><circle cx="20" cy="21" r="18" fill="var(--gold)" stroke="#fff" stroke-width="2"/><path d="M27 21 H13 M18 16 L13 21 L18 26" stroke="#0f1b3d" stroke-width="2" fill="none"/><circle cx="70" cy="21" r="18" fill="var(--blue)" stroke="#fff" stroke-width="2"/><path d="M63 21 H77 M72 16 L77 21 L72 26" stroke="#fff" stroke-width="2" fill="none"/></svg>
</section>

<!-- TRUSTED -->
<section>
  <h2 class="section-title" style="top:3412px">Trusted by Leading Organizations</h2>
  <p class="section-sub" style="top:3476px">Join hundreds of companies improving customer loyalty with PollMeridian</p>
  <div class="logo-box" style="left:142px"><i></i>Halvex</div>
  <div class="logo-box" style="left:299px"><i></i>Fjordline</div>
  <div class="logo-box" style="left:455px"><i></i>Brightmoor</div>
  <div class="logo-box" style="left:610px"><i></i>Kestrel</div>
  <div class="logo-box" style="left:766px"><i></i>Vantor</div>
  <div class="logo-box" style="left:923px"><i></i>Oreline</div>
  <svg class="abs" style="left:550px;top:3637px" width="100" height="20" viewBox="0 0 100 20"><g fill="#8a93aa"><circle cx="10" cy="10" r="2.5"/><circle cx="30" cy="10" r="2.5"/><circle cx="70" cy="10" r="2.5"/><circle cx="90" cy="10" r="2.5"/></g><circle cx="50" cy="10" r="6" fill="none" stroke="var(--blue)" stroke-width="1.5"/><circle cx="50" cy="10" r="2.5" fill="var(--blue)"/></svg>
</section>

<!-- CTA -->
<section class="cta">
  <h2>Ready to Transform<br>Your <b>Customer Experience?</b></h2>
  <p>See how PollMeridian can help you collect better feedback, gain deeper insights, and drive measurable improvements in customer loyalty.</p>
  <div class="btn" style="left:292px;top:252px;width:176px;background:#fff;color:var(--navy)">Schedule Free Demo</div>
  <div class="btn" style="left:482px;top:252px;width:146px;border:1.5px solid #fff;color:#fff">View Pricing</div>
</section>

<!-- FOOTER -->
<footer class="footer">
  <div class="brand abs" style="left:142px;top:64px;color:#8fc0ff"><span class="brand-dot"></span>Lumora CX</div>
  <div class="abs" style="left:142px;top:148px;width:270px;font-size:11.5px;line-height:19px;color:#dfe6f5">Latest Updates, Exclusive Content, And Special Offers? Subscribe To Our Newsletter!</div>
  <div class="abs" style="left:142px;top:202px;width:264px;height:34px;border-radius:17px;background:#fff;font-size:11px;color:#8a93aa;padding:10px 16px">✉ Your Email</div>
  <svg class="abs" style="left:372px;top:205px" width="28" height="28" viewBox="0 0 28 28"><circle cx="14" cy="14" r="13" fill="var(--blue)"/><path d="M8 14 H20 M15 9 L20 14 L15 19" stroke="#fff" stroke-width="2" fill="none"/></svg>

  <h4 style="left:498px">Quick Links</h4>
  <ul style="left:500px"><li>Home</li><li>Product</li><li>About</li><li>Resources</li><li>Pricing</li><li>Contac</li></ul>

  <h4 style="left:684px">Contact Details</h4>
  <svg class="abs" style="left:684px;top:114px" width="12" height="14" viewBox="0 0 12 14"><path d="M6 13 C2 8 1 6 1 5 A5 5 0 0 1 11 5 C11 6 10 8 6 13Z" fill="#fff"/></svg>
  <div class="fcontact" style="left:706px;top:110px">48 Harbor Lane, Suite 210<br>Eastfield, ST 10482<br>United States</div>
  <svg class="abs" style="left:684px;top:172px" width="13" height="13" viewBox="0 0 13 13"><path d="M2 1 L5 1 L6 4 L4 5 Q5 8 8 9 L9 7 L12 8 L12 11 Q6 13 1 4Z" fill="#fff"/></svg>
  <div class="fcontact" style="left:706px;top:168px">Phone<br>+00 555 0192</div>
  <svg class="abs" style="left:684px;top:228px" width="14" height="11" viewBox="0 0 14 11"><rect x="0.5" y="0.5" width="13" height="10" fill="#fff"/><path d="M1 1 L7 6 L13 1" stroke="#0f2249" fill="none"/></svg>
  <div class="fcontact" style="left:706px;top:224px">Email<br>info@lumoracx.example</div>

  <h4 style="left:956px">Social Media</h4>
  <div class="social" style="top:112px"><i style="background:var(--gold);border-color:var(--gold)"></i>Social One</div>
  <div class="social" style="top:153px"><i></i>Video Channel</div>
  <div class="social" style="top:194px"><i></i>Pro Network</div>
  <div class="social" style="top:235px"><i></i>Photo Feed</div>

  <div class="abs" style="left:142px;top:311px;width:918px;height:1px;background:#2e416a"></div>
  <div class="abs" style="left:142px;top:345px;font-size:12px;color:#dfe6f5">© 2025 Lumora CX. All Rights Reserved.</div>
  <div class="abs" style="left:842px;top:339px;font-size:12px;color:#dfe6f5">Privacy Policy &nbsp;|&nbsp; Terms Of Service</div>
</footer>

</body>
</html>
```